Internal Designs and HTML Prototype

A Home page design has been completed. The remaining 6 pages need to be designed based on the provided wireframes and the home page design. HTML conversion to be performed to the following standards; - XHTML 1.0 Transitional - Fixed width - Cross-browser compatibility - Safari 2&3, Opera 9 etc - Relative Font sizes - Table-less forms - JQuery as preferred Javascript library - SEO and loading optimoisation

The selected designer will be required to provide the HTML prototype for their layouts.

Target Market(s)

Ensure style of provided Home page is followed.

Industry/Entity Type

Real Estate

```html
<!DOCTYPE html>
<html lang="en">
<head>
<meta charset="utf-8">
<title>Tradenest – Property Edit</title>
<link rel="stylesheet" href="https://fonts.googleapis.com/css2?family=Arimo:wght@400;700&display=swap">
<style>
:root{
  --orange:#f26a1b;
  --orange-line:#f0844a;
  --arrow-box:#d9703f;
  --band-top:#f04a24;
  --band-bottom:#d92f16;
  --sage:#6c8a72;
  --sage-dark:#56705b;
  --page-bg:#dcedc8;
  --peach:#fde0c4;
  --ink:#1e1e1e;
  --white:#ffffff;
}
*{box-sizing:border-box;margin:0;padding:0}
html,body{width:675px;height:1200px;overflow:hidden;background:var(--page-bg)}
.page{width:800px;height:1423px;transform:scale(.84375);transform-origin:0 0;position:relative;background:var(--page-bg);font-family:"Arimo",Arial,sans-serif;color:var(--ink)}
.header-photo{position:absolute;left:0;top:0;width:800px;height:138px;background:linear-gradient(100deg,#2f5a1e 0%,#4f8a2e 40%,#6aa23c 70%,#8fbf5a 100%)}
.brand{position:absolute;left:26px;top:24px;display:flex;align-items:center;gap:10px;height:92px}
.brand-square{width:22px;height:22px;background:var(--orange)}
.brand-name{font-size:40px;font-weight:700;color:var(--white)}
.band{position:absolute;left:0;top:138px;width:800px;height:37px;background:linear-gradient(var(--band-top),var(--band-bottom));border-bottom:3px solid #fff}
.tagline{position:absolute;left:22px;top:7px;font-size:19px;color:var(--white)}
.login{position:absolute;left:456px;top:12px;display:flex;align-items:center;gap:4px;font-size:7px;font-weight:700;color:var(--white);letter-spacing:.3px}
.login input{width:86px;height:11px;border:1px solid #ccc;background:#fff;margin-right:4px}
.login .signin{background:var(--sage);border:1px solid #fff;color:#fff;font-size:7px;padding:1px 6px;font-weight:700}
.nav{position:absolute;left:12px;top:192px;width:96px}
.nav a{display:flex;align-items:center;justify-content:center;text-align:center;height:56px;margin-bottom:6px;background:var(--sage);border:2px solid #e4eee0;border-right:none;border-radius:8px 0 0 8px;color:var(--white);font-size:14px;line-height:18px;text-decoration:none;letter-spacing:-.3px}
.panel{position:absolute;left:106px;top:190px;width:684px;height:1208px;background:var(--sage);border-radius:12px;padding:7px 8px 7px 6px}
.panel-inner{width:100%;height:100%;background:linear-gradient(90deg,#fff 0%,#fff 45%,var(--peach) 100%);border-radius:8px;padding:0 18px 0 24px;position:relative}
.page-head{display:flex;justify-content:space-between;align-items:flex-end;padding-top:38px}
.page-title{font-size:19px;font-weight:700;color:var(--orange)}
.account-links{font-size:11px;color:var(--orange);margin-bottom:3px}
.account-links a{color:var(--orange)}
.subtitle{font-size:13px;font-weight:700;color:var(--sage);margin-top:30px}
.fields{display:grid;grid-template-columns:192px 192px 192px;column-gap:24px;margin-top:14px}
.field{height:52px}
.field.tall{height:104px}
.label{font-size:8.5px;letter-spacing:.5px;display:block;height:9px;text-transform:uppercase}
.input,.select,.area{display:block;height:21px;border:1px solid var(--orange-line);background:#fff;position:relative;font-size:8.5px;padding:5px 0 0 4px;color:#555}
.select::after{content:"";position:absolute;right:1px;top:1px;width:16px;height:17px;background:var(--arrow-box);border:1px solid #a9532a}
.select::before{content:"";position:absolute;right:6px;top:8px;border:3px solid transparent;border-top:4px solid #222;z-index:1}
.area{height:73px}
.area::after{content:"";position:absolute;right:1px;top:1px;width:15px;height:69px;background:var(--orange);border-left:1px solid #c85a26}
.input-wide{width:192px}
.group-title{font-size:8.5px;letter-spacing:.5px;border-bottom:1px solid var(--orange-line);padding-bottom:4px;margin-top:22px}
.checks{display:grid;grid-template-columns:216px 218px 192px;margin-top:14px;row-gap:9px}
.check{font-size:8.5px;letter-spacing:.5px;display:flex;align-items:center;gap:5px;height:11px}
.check::before{content:"";width:9px;height:9px;border:1px solid var(--orange-line);background:#fff}
.actions{display:flex;gap:10px;margin-top:30px}
.btn{background:var(--orange);color:#fff;font-size:10px;font-weight:700;border:1px solid #d85a1a;border-radius:3px;padding:5px 8px;box-shadow:0 1px 2px rgba(0,0,0,.3)}
</style>
</head>
<body>
<div class="page">
  <div class="header-photo" role="img" aria-label="Family relaxing on a green lawn"></div>
  <div class="brand"><span class="brand-square"></span><span class="brand-name">tradenest</span></div>
  <div class="band">
    <div class="tagline">The place to sell. The place to buy.</div>
    <div class="login">USER NAME <input> PASSWORD <input> <span class="signin">SIGN IN</span></div>
  </div>
  <nav class="nav">
    <a>Home</a><a>Property<br>Search</a><a>How<br>It Works</a><a>My<br>Account</a><a>Contact</a>
  </nav>
  <main class="panel"><div class="panel-inner">
    <div class="page-head">
      <h1 class="page-title">PROPERTY EDIT</h1>
      <div class="account-links"><a>Registration Details</a> | <a>My Properties</a> | <a>My Messages</a> | <a>My Shortlist</a></div>
    </div>
    <h2 class="subtitle">Update property details</h2>
    <div class="fields">
      <div class="field"><span class="label">Title</span><span class="select"></span></div>
      <div class="field"><span class="label">Property</span><span class="input"></span></div>
      <div class="field"></div>
      <div class="field tall"><span class="label">Short Description</span><span class="area"></span></div>
      <div class="field tall"><span class="label">Description</span><span class="area"></span></div>
      <div class="field tall"><span class="label">Address</span><span class="area"></span></div>
      <div class="field"><span class="label">Unit</span><span class="select">ANY</span></div>
      <div class="field"><span class="label">Suburb</span><span class="select"></span></div>
      <div class="field"><span class="label">Price</span><span class="input"></span></div>
      <div class="field"><span class="label">No. of Bathrooms</span><span class="select">ANY</span></div>
      <div class="field"><span class="label">No. of Bedrooms</span><span class="select"></span></div>
      <div class="field"><span class="label">No. of Levels</span><span class="select"></span></div>
      <div class="field"><span class="label">No. of Carspaces</span><span class="select"></span></div>
      <div class="field"><span class="label">Building Size</span><span class="select"></span></div>
      <div class="field"><span class="label">Land Size</span><span class="select"></span></div>
      <div class="field"><span class="label">Year Built</span><span class="select"></span></div>
    </div>
    <div class="group-title" style="margin-top:0">INTERIOR</div>
    <div class="checks">
      <span class="check">CENTRAR AIR-CONDITIONING</span><span class="check">FURNISHED</span><span class="check">SWIMMING POOL</span>
      <span class="check">DISABILITY FEATURES</span><span class="check">GAS/WOOD FIREPLACE</span><span class="check">WHEELCHAIR ACCESS</span>
      <span class="check">ELEVATOR</span><span class="check">SPA/JACUZZI</span><span class="check">GAS RANGE</span>
    </div>
    <div class="group-title">COUNTER</div>
    <div class="checks">
      <span class="check">GRANITE COUNTER</span><span class="check">LAMINATE</span><span class="check">MARBLE</span>
      <span class="check">ENGINEERED STONE</span><span class="check">WOOD/BUTCHER BLOCK</span><span class="check">CONCRETE</span>
      <span class="check">SOLID SURFACE</span><span class="check">STAINLESS STEEL</span><span class="check">OTHER</span>
      <span class="check">CERAMIC TILE</span>
    </div>
    <div class="group-title">FLOORING TYPE</div>
    <div class="checks">
      <span class="check">CARPETED</span><span class="check">STONE</span><span class="check">VINYL</span>
      <span class="check">TILES</span><span class="check">LAMINATE</span><span class="check">OTHE</span>
      <span class="check">HARDWOOD</span>
    </div>
    <div class="group-title">ROOMS</div>
    <div class="checks">
      <span class="check">BASEMENT</span><span class="check">COURTYARD/PATIO</span><span class="check">STUDY/OFFICE</span>
      <span class="check">FORMAL LIVING ROOM</span><span class="check">THEATRE ROOM</span>
    </div>
    <div class="group-title">EXTERIOR FEATURES</div>
    <div class="checks">
      <span class="check">RIVER VIEW</span><span class="check">PARK VIEW</span><span class="check">FARM ANIMALS</span>
      <span class="check">OCEAN FRONT</span><span class="check">CITY VIEW</span><span class="check">BALCONY</span>
      <span class="check">OCEAN VIEW</span><span class="check">MOUNTAIN VIEW</span><span class="check">WATER TANK</span>
      <span class="check">LAKE FRONT</span><span class="check">WATER ACCESS</span><span></span>
      <span class="check">LAKE VIEW</span><span class="check">ANIMALS ALLOWED</span>
    </div>
    <div class="group-title">NEIGHBORHOOD FEATURES</div>
    <div class="checks">
      <span class="check">GOLF COURSE</span><span class="check">MARINA</span><span class="check">PLAYGROUND/PARK</span>
      <span class="check">RECREATION HALL</span><span class="check">FITNESS CENTRE</span><span class="check">PUBLIC TRANSPORT</span>
      <span class="check">SECURITY GATES</span><span class="check">SECURITY GUARD</span><span class="check">HEALTHCARE CENTRE/HOSPITAL</span>
    </div>
    <div class="actions"><span class="btn">CANCEL</span><span class="btn">CONTINUE</span></div>
  </div></main>
</div>
</body>
</html>
```